Business Card Design for Mabel's Larder

We make food for dogs.
Business Card Design (using the logo designed by you). Our Brand color is a bright canary yellow. For example our signage is predominantly yellow, with the logo in black. I'd like the card also to use that imagery.
Feel free to use the two sides creatively.
Vertical Design is also great.

Industry/Entity Type

Pet food

Contact Information for Business Card

Name, email, website, phone no

Font styles to use
Sans Serif

Colors
59FF00
82FF00
B8FF75
E3FFCB
F4FFEA
FFF300
FFF600
FEFA6F
FFFEC7
FFFEE8

Requirements
Nice to have
• A graphic in the same brush stroke style of the logo shoeing a doggy bowl of food

```html
<!DOCTYPE html>
<html lang="en">
<head>
<meta charset="utf-8">
<title>Mabel's Larder — Business Card</title>
<link rel="stylesheet" href="https://fonts.googleapis.com/css2?family=Oswald:wght@500&family=Montserrat:wght@400;700&display=swap">
<style>
  :root {
    --canvas: #d6d6d6;
    --canary: #ffe253;
    --ink: #111111;
    --black: #000000;
    --text-dark: #2a2a2a;
  }
  * { margin: 0; padding: 0; box-sizing: border-box; }
  html, body { width: 1200px; height: 913px; overflow: hidden; }
  body {
    background: var(--canvas);
    position: relative;
    font-family: "Montserrat", sans-serif;
  }
  .card {
    position: absolute;
    top: 301px;
    width: 540px;
    height: 310px;
    overflow: hidden;
    box-shadow: 0 14px 30px rgba(0,0,0,0.35);
  }
  .card--front { left: 40px; background: var(--canary); color: var(--ink); }
  .card--back { left: 620px; background: var(--black); }

  .front-details {
    position: absolute;
    left: 34px;
    top: 40px;
    width: 300px;
  }
  .brand-title {
    font-family: "Oswald", sans-serif;
    font-weight: 500;
    font-size: 40px;
    line-height: 1;
    letter-spacing: 0.5px;
    text-transform: uppercase;
    color: var(--ink);
  }
  .person-name {
    margin-top: 22px;
    font-weight: 700;
    font-size: 21px;
    text-transform: uppercase;
    color: var(--text-dark);
    letter-spacing: -0.3px;
  }
  .person-role {
    font-size: 13px;
    color: var(--text-dark);
    margin-top: 2px;
  }
  .contact-list { list-style: none; margin-top: 12px; }
  .contact-item {
    display: flex;
    align-items: flex-start;
    gap: 10px;
    font-size: 12.5px;
    line-height: 1.45;
    color: var(--text-dark);
  }
  .contact-icon { width: 12px; height: 12px; margin-top: 3px; flex: none; }
  .contact-icon--blank { visibility: hidden; }

  .front-accent {
    position: absolute;
    right: -90px;
    top: -40px;
    width: 300px;
    height: 300px;
    border-radius: 50%;
    background: var(--ink);
  }

  .back-lockup {
    position: absolute;
    inset: 0;
    display: flex;
    align-items: center;
    justify-content: center;
    gap: 14px;
  }
  .back-mark {
    width: 26px;
    height: 26px;
    border-radius: 50%;
    background: var(--canary);
  }
  .back-name {
    font-family: "Oswald", sans-serif;
    font-weight: 500;
    font-size: 50px;
    letter-spacing: 1px;
    text-transform: uppercase;
    color: var(--canary);
  }
</style>
</head>
<body>
  <section class="card card--front">
    <div class="front-accent" aria-hidden="true"></div>
    <div class="front-details">
      <h1 class="brand-title">Mabel's Larder</h1>
      <p class="person-name">Arthur Benson</p>
      <p class="person-role">Managing Director</p>
      <ul class="contact-list">
        <li class="contact-item">
          <svg class="contact-icon" viewBox="0 0 24 24"><path fill="#2a2a2a" d="M6.6 10.8a15.1 15.1 0 0 0 6.6 6.6l2.2-2.2c.3-.3.7-.4 1-.2 1.1.4 2.3.6 3.6.6.6 0 1 .4 1 1V20c0 .6-.4 1-1 1A17 17 0 0 1 3 4c0-.6.4-1 1-1h3.5c.6 0 1 .4 1 1 0 1.3.2 2.5.6 3.6.1.3 0 .7-.2 1z"/></svg>
          <span>044-321 654 987</span>
        </li>
        <li class="contact-item">
          <svg class="contact-icon" viewBox="0 0 24 24"><path fill="#2a2a2a" d="M2 5h20v14H2z"/><path fill="none" stroke="#ffe253" stroke-width="1.6" d="M2 5l10 8 10-8"/></svg>
          <span>hello@mabelslarder.com</span>
        </li>
        <li class="contact-item">
          <svg class="contact-icon" viewBox="0 0 24 24"><circle cx="12" cy="12" r="10" fill="#2a2a2a"/><path fill="none" stroke="#ffe253" stroke-width="1.4" d="M2 12h20M12 2c3 3 3 17 0 20M12 2c-3 3-3 17 0 20"/></svg>
          <span>www.mabelslarder.com</span>
        </li>
        <li class="contact-item">
          <svg class="contact-icon contact-icon--blank" viewBox="0 0 24 24"></svg>
          <span>17, Orchard Row here<br>Dunmore Vale, 30218</span>
        </li>
      </ul>
    </div>
  </section>

  <section class="card card--back">
    <div class="back-lockup">
      <span class="back-mark" aria-hidden="true"></span>
      <span class="back-name">Mabel's Larder</span>
    </div>
  </section>
</body>
</html>
```